Webshop-Design für Sport- und Fitnesslabel
Zielgruppe
Zack los! ist ein dynamisches Sport – und Fitnesslabel, mit Schwerpunkt im Textilbereich – aber auch mit weiteren Sparten (Sport Drinks etc.). Wir bieten top Qualität mit idealer Passform zu top Preisen und super Tragekomfort.
Zack los ! steht für Kraft und Dynamik und wir arbeiten nur mit zertifizierten Händlern zusammen – quasi nachhaltig.
Wir sind frisch, cool und transportieren einen Fashion / Lifestyle, der jedermann anspricht – ob in der Freizeit oder im Gym – immer perfekt stylisch unterwegs. Wir wollen europaweit unsere Marke vertreiben.
Zack los! soll es schaffen seinen Kunden ein besonderes Erlebnis, Gefühl oder Produkt zu liefern. Zack los! steht für Vertrauen, Transparenz, Authentizität.
Aufgabenstellung
Die Webshops
https://vernatek.com/
https://ulvy.shop/
https://www.fernwalder.com/
https://www.joraswillet.de/groessenberater/
sollen zur Orientierung dienen. Ein Firmenlogo existiert.
Es soll eine Startseite, eine Artikelübersichtsseite und Artikeldetailseite erstellt werden.
Gerne kann der Designer nach geeigneten Bildern suchen.

```html
<!DOCTYPE html>
<html lang="de">
<head>
<meta charset="utf-8">
<title>Zack los! – T-Shirt XY Marke</title>
<link rel="stylesheet" href="https://fonts.googleapis.com/css2?family=Montserrat:wght@300;400;500;600;700;800;900&family=Open+Sans:wght@300;400&display=swap">
<style>
:root{
  --orange:#d4560f;
  --black:#0a0a0a;
  --ink:#111;
  --grey:#777;
  --line:#bdbdbd;
  --white:#fff;
}
*{box-sizing:border-box;margin:0;padding:0}
html,body{width:1200px;height:2774px;overflow:hidden;background:var(--white)}
body{position:relative;font-family:'Montserrat',sans-serif;color:var(--ink)}
.abs{position:absolute}
/* header */
.site-header{position:absolute;left:0;top:0;width:1200px;height:106px;border-bottom:1px solid var(--line)}
.brand{position:absolute;left:41px;top:31px;font-weight:900;font-size:31px;letter-spacing:-0.5px;color:var(--ink);display:flex;align-items:center;gap:8px}
.brand-dot{width:10px;height:10px;background:var(--orange)}
.main-nav a{position:absolute;top:42px;font-family:'Open Sans',sans-serif;font-weight:300;font-size:21px;color:#777;text-decoration:none}
.main-nav a.active{color:var(--ink);font-weight:400}
.header-icon{position:absolute;top:41px}
/* product imagery */
.photo-man{background:
  radial-gradient(ellipse 45% 55% at 48% 60%,#1c1c1c 0%,#1c1c1c 60%,rgba(28,28,28,0) 62%),
  radial-gradient(ellipse 60% 70% at 50% 45%,#9c9c9c,#7a7a7a)}
.photo-woman{background:
  linear-gradient(180deg,rgba(0,0,0,0) 78%,#6d8fb5 80%,#5a7aa0 100%),
  radial-gradient(ellipse 32% 42% at 52% 55%,#161616 0%,#161616 62%,rgba(22,22,22,0) 65%),
  linear-gradient(160deg,#e0ad8f,#c8906f)}
.photo-shorts{background:
  radial-gradient(ellipse 24% 32% at 50% 48%,#161616 0%,#161616 65%,rgba(22,22,22,0) 68%),
  radial-gradient(circle at 50% 45%,#4a4a4a,#202020)}
.product-photo{position:absolute;left:90px;top:198px;width:510px;height:635px;border:1px solid #999}
.thumb{position:absolute;top:865px;width:115px;height:158px;border:1px solid #999}
.category{left:692px;top:199px;font-weight:600;font-size:18px}
.product-title{left:688px;top:220px;font-weight:700;font-size:33px}
.price{left:692px;top:259px;font-weight:700;font-size:35px;color:var(--orange)}
.tax{left:692px;top:301px;font-size:16px;line-height:19px}
.pill{position:absolute;height:50px;border:3px solid var(--ink);border-radius:25px;display:flex;align-items:center;padding-left:19px;font-weight:500;font-size:16px;gap:8px}
.qty-box{width:27px;height:25px;border:1px solid var(--ink);display:flex;align-items:center;justify-content:center;font-size:15px}
.cart-btn{position:absolute;left:692px;top:527px;width:376px;height:77px;background:var(--orange);color:var(--white);font-weight:700;font-size:23px;display:flex;align-items:center;justify-content:center}
.payments{position:absolute;left:706px;top:636px;width:216px;display:grid;grid-template-columns:1fr 1fr;row-gap:22px;column-gap:14px}
.pay{display:flex;align-items:center;gap:7px;font-weight:600;font-size:16px;color:var(--ink)}
.pay i{width:10px;height:10px;background:var(--orange);display:inline-block}
.description{position:absolute;left:687px;top:778px;width:376px;height:245px;border:2px solid var(--ink);border-radius:20px;padding:17px 19px}
.description h3{font-weight:500;font-size:16px}
.description p{margin-top:32px;font-size:12.6px;line-height:15.6px}
.rule{position:absolute;left:0;width:1200px;height:1px;background:var(--line)}
/* bestsellers */
.section-title{position:absolute;left:0;width:1200px;top:1172px;text-align:center;font-weight:600;font-size:38px}
.card-img{position:absolute;top:1286px;width:262px;height:326px}
.card-name{position:absolute;top:1630px;font-weight:600;font-size:16px}
.dot{position:absolute;top:1696px;width:74px;height:4px;background:#ccc}
.dot.active{background:var(--ink)}
/* banner */
.banner{position:absolute;left:0;top:1799px;width:1200px;height:565px;background:
  radial-gradient(ellipse 18% 10% at 87% 30%,rgba(255,255,255,.35),rgba(255,255,255,0)),
  radial-gradient(ellipse 18% 30% at 42% 50%,#b9c3c4,rgba(185,195,196,0) 70%),
  linear-gradient(100deg,#1a1a1a 0%,#5c5c5c 30%,#8a8a8a 45%,#4a4a4a 65%,#262626 100%)}
.banner-title{position:absolute;left:57px;top:2115px;color:var(--white);font-weight:800;font-size:37px;line-height:42px}
.banner-btn{position:absolute;left:53px;top:2224px;width:245px;height:64px;background:var(--orange);color:var(--white);font-weight:700;font-size:20px;display:flex;align-items:center;justify-content:center}
/* footer */
.site-footer{position:absolute;left:0;top:2364px;width:1200px;height:336px;background:var(--black);color:var(--white)}
.footer-bar{position:absolute;left:66px;top:2355px;width:1079px;height:16px;background:var(--orange)}
.footer-edge{position:absolute;left:47px;top:2364px;width:1px;height:336px;background:#444}
.foot-h{position:absolute;font-weight:400;font-size:22px;color:var(--white)}
.foot-l{position:absolute;font-weight:300;font-size:15px;color:#bbb}
.social{position:absolute;top:2603px;font-size:15px;font-weight:500;color:var(--white);display:flex;align-items:center;gap:7px}
.social i{width:22px;height:22px;border-radius:50%;background:var(--white);display:inline-block}
.news-input{position:absolute;left:853px;top:2579px;width:291px;height:47px;background:var(--white);color:#777;font-weight:300;font-size:15px;display:flex;align-items:center;padding-left:17px}
.legal{position:absolute;top:2730px;font-size:10px;font-weight:500}
</style>
</head>
<body>

<header class="site-header">
  <div class="brand">Zack los! <span class="brand-dot"></span></div>
  <nav class="main-nav">
    <a style="left:291px">FRAUEN</a>
    <a class="active" style="left:456px">MÄNNER</a>
    <a style="left:630px">ACCESSOIRES</a>
    <a style="left:843px">DRINKS</a>
  </nav>
  <svg class="header-icon" style="left:1020px" width="24" height="24" viewBox="0 0 24 24" fill="none" stroke="#111" stroke-width="2"><circle cx="10" cy="10" r="7"/><line x1="15" y1="15" x2="21" y2="21"/></svg>
  <svg class="header-icon" style="left:1073px" width="26" height="24" viewBox="0 0 26 24" fill="none" stroke="#111" stroke-width="2"><path d="M13 21 L3 11 A5.5 5.5 0 0 1 13 4 A5.5 5.5 0 0 1 23 11 Z"/></svg>
  <svg class="header-icon" style="left:1128px" width="26" height="24" viewBox="0 0 26 24" fill="none" stroke="#111" stroke-width="2"><path d="M2 3h4l3 12h12l2-8H7"/><circle cx="10" cy="20" r="1.6"/><circle cx="20" cy="20" r="1.6"/></svg>
</header>

<main>
  <div class="product-photo photo-man" role="img" aria-label="Mann in schwarzem T-Shirt vor grauer Wand"></div>
  <div class="thumb photo-man" style="left:90px" role="img" aria-label="Produktansicht 1"></div>
  <div class="thumb photo-man" style="left:222px" role="img" aria-label="Produktansicht 2"></div>
  <div class="thumb photo-man" style="left:353px" role="img" aria-label="Produktansicht 3"></div>
  <div class="thumb photo-man" style="left:485px" role="img" aria-label="Produktansicht 4"></div>

  <div class="abs category">MÄNNER</div>
  <h1 class="abs product-title">T-SHIRT XY MARKE</h1>
  <div class="abs price">34,95 €</div>
  <div class="abs tax">inkl. MwSt<br>zzgl. Versandkosten</div>

  <div class="pill" style="left:687px;top:369px;width:124px">GRÖßE
    <svg width="20" height="12" viewBox="0 0 20 12" fill="none" stroke="#111" stroke-width="2.5"><path d="M2 2l8 8 8-8"/></svg></div>
  <div class="pill" style="left:835px;top:369px;width:122px">FARBE
    <svg width="20" height="12" viewBox="0 0 20 12" fill="none" stroke="#111" stroke-width="2.5"><path d="M2 2l8 8 8-8"/></svg></div>
  <div class="pill" style="left:687px;top:443px;width:217px">ANZAHL
    <svg style="margin-left:8px" width="20" height="12" viewBox="0 0 20 12" fill="none" stroke="#111" stroke-width="2.5"><path d="M2 2l8 8 8-8"/></svg>
    <span class="qty-box">1</span>
    <svg width="20" height="12" viewBox="0 0 20 12" fill="none" stroke="#111" stroke-width="2.5"><path d="M2 10l8-8 8 8"/></svg></div>

  <div class="cart-btn">IN DEN WARENKORB</div>

  <div class="payments" aria-label="Zahlungsarten">
    <div class="pay"><i></i>Paywell</div>
    <div class="pay"><i></i>Varda</div>
    <div class="pay"><i></i>Amerix</div>
    <div class="pay"><i></i>Marlo</div>
    <div class="pay"><i></i>Lastora</div>
  </div>

  <section class="description">
    <h3>BESCHREIBUNG</h3>
    <svg style="position:absolute;right:26px;top:20px" width="22" height="14" viewBox="0 0 22 14" fill="none" stroke="#111" stroke-width="2.5"><path d="M2 12l9-9 9 9"/></svg>
    <p>Lorem ipsum dolor sit amet, consetetur sadipscing elitr, sed diam nonumy eirmod tempor invidunt ut labore et dolore magna aliquyam erat, sed diam voluptua. At vero eos et accusam et justo duo dolores et ea rebum. Stet clita kasd gubergren, no sea takimata sanctus est Lorem ipsum dolor sit amet.<br>sea takimata sanctus est Lorem ipsum dolor sit amet.</p>
  </section>

  <div class="rule" style="top:1105px"></div>

  <h2 class="section-title">Unsere Bestseller</h2>
  <svg class="abs" style="left:22px;top:1430px" width="24" height="40" viewBox="0 0 24 40" fill="none" stroke="#999" stroke-width="3"><path d="M20 2L4 20l16 18"/></svg>
  <svg class="abs" style="left:1159px;top:1430px" width="24" height="40" viewBox="0 0 24 40" fill="none" stroke="#111" stroke-width="3"><path d="M4 2l16 18L4 38"/></svg>

  <div class="card-img photo-man" style="left:65px" role="img" aria-label="Mann in schwarzem T-Shirt"></div>
  <div class="card-img photo-woman" style="left:337px" role="img" aria-label="Frau in schwarzem T-Shirt vor apricotfarbener Wand"></div>
  <div class="card-img photo-shorts" style="left:610px" role="img" aria-label="Schwarze Sportshorts"></div>
  <div class="card-img photo-woman" style="left:882px" role="img" aria-label="Frau in schwarzem T-Shirt vor apricotfarbener Wand"></div>

  <div class="card-name" style="left:70px">Artikelname</div>
  <div class="card-name" style="left:348px">Artikelname</div>
  <div class="card-name" style="left:626px">Artikelname</div>
  <div class="card-name" style="left:903px">Artikelname</div>

  <div class="dot active" style="left:488px"></div>
  <div class="dot" style="left:573px"></div>
  <div class="dot" style="left:658px"></div>

  <div class="rule" style="top:1746px"></div>

  <section class="banner" role="img" aria-label="Sportlerin trinkt im Fitnessstudio"></section>
  <div class="banner-title">UNSERE BRANDNEUEN DRINKS<br>SIND DA!</div>
  <div class="banner-btn">ENTDECKEN</div>
</main>

<footer class="site-footer"></footer>
<div class="footer-edge"></div>
<div class="footer-bar"></div>

<div class="foot-h" style="left:66px;top:2441px">LINKS</div>
<div class="foot-l" style="left:66px;top:2504px">AGB</div>
<div class="foot-l" style="left:66px;top:2537px">Retoure</div>
<div class="foot-l" style="left:66px;top:2570px">Versand- bzw. Lieferbedingungen</div>
<div class="foot-l" style="left:66px;top:2604px">Zahlungsmöglichketein</div>

<div class="foot-h" style="left:447px;top:2441px">KONTAKT</div>
<div class="foot-l" style="left:447px;top:2504px">info@zack-los.de</div>
<div class="foot-h" style="left:447px;top:2551px">SOCIAL MEDIA</div>
<div class="social" style="left:447px"><i></i>Facelink</div>
<div class="social" style="left:560px"><i></i>Snapgram</div>

<div class="foot-h" style="left:853px;top:2441px">NEWSLETTER</div>
<div class="foot-l" style="left:853px;top:2503px;width:300px;font-size:14.4px;line-height:18px">Melde dich jetzt für den Newsletter an und sichere dir 15% auf deinen nächsten Einkauf! Ohne Mindestbestellwert.</div>
<div class="news-input">DEINE MAILADRESSE
  <svg style="position:absolute;right:18px;top:16px" width="10" height="16" viewBox="0 0 10 16" fill="none" stroke="#111" stroke-width="2"><path d="M2 2l6 6-6 6"/></svg></div>

<div class="legal" style="left:529px">COPYRIGHT - ZACK LOS ! 2020</div>
<div class="legal" style="left:955px">DATENSCHUTZ</div>
<div class="legal" style="left:1067px">IMPRESSUM</div>

</body>
</html>
```